Website design for Brelvo Quad

Full Website Content Draft for: 'Brelvo Quad - A Financial Freedom Movement'

Header / Navigation
Logo (top left)
Navigation Links: Home | Our Story | Current State | Future State | How You Can Help | The Movement | Get Involved
CTA Button: Join the Movement
Homepage (Hero Section)

Headline:
Empowering Students. Transforming Futures.
Sub-Headline:
Financial literacy isn’t optional anymore — it’s essential.
Body (short):
Every year, millions of college students step into adulthood without the skills to manage money wisely. It’s time to change that.
Call-to-Action Button:
[Join the Movement]
Visual Suggestion:
Full-width image/video of diverse students on campus — upbeat, collaborative, inspiring.
Our Story

Section Header: Our Story
Body Copy:
For too long, financial literacy has been the missing piece of higher education. While students prepare academically for their futures, many graduate with financial stress, poor money habits, and debt that follows them for decades.
We believe knowledge is power — and financial literacy is freedom. With decades of combined experience in banking, leadership, and higher education, our team has seen the struggles firsthand. That’s why we’re committed to starting a movement that ensures every student leaves college not only with a degree, but with financial confidence.
The Current State

Section Header: The Current State
Infographic Copy / Stats:
70% of college students report finances as their #1 source of stress.*
43% of students don’t know their credit score.**
Student loan debt has surpassed $1.7 trillion.***
Subtext:
This is today’s reality. Students deserve better.
Footnotes (to place at bottom of page):
* Norwell Scholastic Wellness Guild, Kestrin Student Vitality Survey, Spring 2022 Report.
** DALMOR & Pexton Pension Partners, Coins Count at School Review (2019).
*** Quillan Monetary Trust of Harbridge, Consumer Credit Data (2024).
Visual Suggestion:
Infographic row with 3 icons (stress, credit, debt) and corresponding stats.
The Future State (Vision)

Section Header: The Future State (Vision)
Body Copy:
Imagine a campus where students graduate with more than a degree — they graduate with financial confidence.
They know how to budget, save, manage credit, and plan for their futures. They are free from fear, better equipped for life after graduation, and ready to thrive personally and professionally.
This is the future we are building together.
Visual Suggestion:
Smiling students celebrating graduation, overlay text “Confidence. Knowledge. Freedom.”
How You Can Help

Section Header: How You Can Help
Copy with Columns:
Universities
Partner with us to bring scalable, student-centered financial education to your campus.
Banks & Financial Institutions
Join us in shaping the next generation of financially confident customers while strengthening community impact.
Students & Parents
Be part of a movement that makes the college experience stronger, not harder.
Call-to-Action Button:
[Contact Us to Partner]
Visual Suggestion:
Three-column layout with icons (graduation cap for Universities, bank building for Banks, heart/people for Students & Parents).
The Movement

Section Header: The Movement
Body Copy:
This isn’t about one campus — it’s about a shift. A national movement to change the financial future for an entire generation. Together, we can rewrite the story.
We believe when students understand money, they reduce stress, gain freedom, and unlock their potential. That’s why this is more than a program — it’s a movement.
Visual Suggestion:
Map of the U.S. with “movement dots” spreading out, or collage of diverse students with bold words: Financial Literacy. Confidence. Future.
Get Involved (Contact Section)

Section Header: Get Involved
Body Copy:
Are you a university leader, bank executive, student, or parent who wants to be part of this movement? Let’s talk.
Contact Form Fields:
Name
Email
Role (University Faculty/Staff, Bank Partner, Student, Parent, Other)
Message
CTA Button: [Submit Interest]
Footer

Copy:
Join us in building the future of financial literacy.
Links: Privacy | Contact | Social Media (Workloom, Snapvale, etc.)

Target Market(s)

Partners: University Faculty and Bank Executives

Industry/Entity Type

Finance and Education

Coding

Number of Pages Required

4 page

Font styles to use
Sans Serif

Colors

Designer to choose colors to be used in the design.

Requirements
Nice to have
• See description for details - This is a website to create a "movement" to help college and university students increase their financial literacy and reduce financial stress,

```html
<!DOCTYPE html>
<html lang="en">
<head>
<meta charset="utf-8">
<title>Brelvo Quad – A Financial Freedom Movement</title>
<link rel="stylesheet" href="https://fonts.googleapis.com/css2?family=Lexend:wght@300;400;500&family=Inter:wght@400;500;600&display=swap">
<style>
:root{
  --ink:#1d1d1f;
  --ink-soft:#4a4a4e;
  --white:#ffffff;
  --paper:#f7f7f9;
  --sand:#f3f3f0;
  --night:#1c1c1c;
  --blue:#1f4fb0;
  --blue-soft:#d9def3;
  --field:#e2e2e0;
  --card-warm:#f5f1ec;
  --card-grey:#ebebed;
}
*{box-sizing:border-box;margin:0;padding:0}
html,body{width:1200px;height:4822px;overflow:hidden}
body{background:var(--paper);color:var(--ink);font-family:"Inter",Arial,sans-serif;position:relative}
.heading{font-family:"Lexend",Arial,sans-serif;font-weight:400}
section,header,footer{position:absolute;left:0;width:1200px}

/* Hero */
.hero{top:0;height:595px;overflow:hidden}
.hero-photo{position:absolute;inset:0;background:linear-gradient(100deg,#2b2a27 0%,#4b4236 35%,#6d5a45 60%,#3a3b32 100%)}
.hero-shade{position:absolute;inset:0;background:linear-gradient(90deg,rgba(10,10,14,.65) 0%,rgba(10,10,14,.35) 60%,rgba(10,10,14,.2) 100%)}
.nav{position:absolute;top:22px;left:4px;right:30px;display:flex;align-items:center}
.brand{font-family:"Lexend",sans-serif;font-weight:500;font-size:30px;color:var(--white);letter-spacing:-.5px;width:160px}
.nav-links{display:flex;gap:22px;list-style:none;font-size:12px;color:var(--white)}
.nav-cta{margin-left:auto;background:var(--blue);color:var(--white);font-size:11px;padding:8px 14px;border-radius:3px}
.hero-copy{position:absolute;left:40px;top:228px;width:560px;color:var(--white)}
.hero-copy h1{font-size:52px;line-height:56px;font-weight:400}
.hero-copy p{margin-top:20px;font-size:15px;line-height:24px}
.btn{display:inline-block;background:var(--blue);color:var(--white);font-size:13px;padding:11px 16px;border-radius:3px}
.hero-copy .btn{margin-top:24px}

/* Story */
.story{top:595px;height:551px;background:var(--paper)}
.story h2{position:absolute;left:44px;top:braces;}
.story h2{top:26px;font-size:48px;line-height:56px}
.story .body{position:absolute;left:42px;top:180px;width:700px;font-size:21px;line-height:28px;color:var(--ink)}
.story .body p+p{margin-top:28px}
.story-photo{position:absolute;left:34px;top:551px;width:838px;height:470px;border-radius:14px;background:linear-gradient(160deg,#6f8a5a 0%,#8a7a62 45%,#b5766a 75%,#a88f7a 100%);z-index:2}

/* Current state */
.current{top:1146px;height:975px;background:var(--sand)}
.current h2{position:absolute;left:26px;top:516px;font-size:27px}
.stats{position:absolute;left:26px;top:560px;display:flex;gap:23px}
.stat{width:266px}
.stat-card{height:266px;background:var(--white);border-radius:10px;padding:30px}
.stat-icon{width:100%;height:100%;background:linear-gradient(180deg,#efefef,#e4e4e4);border-radius:6px}
.stat-value{margin-top:22px;font-family:"Lexend",sans-serif;font-size:17px}
.stat-note{margin-top:10px;font-size:10px;line-height:15px;color:var(--ink-soft)}

/* Future */
.future{top:2121px;height:744px;background:var(--night);color:var(--white)}
.future h2{position:absolute;left:26px;top:76px;font-size:40px}
.future .body{position:absolute;left:26px;top:160px;width:560px;font-size:16px;line-height:22.5px}
.future-photo{position:absolute;top:331px;height:390px;border-radius:6px}
.fp1{left:0;width:343px;border-radius:0 6px 6px 0;background:linear-gradient(135deg,#4a5a72,#8a7b6a 55%,#c2a989)}
.fp2{left:365px;width:394px;background:linear-gradient(160deg,#5f7a4e,#7c6d5a 55%,#a58a6e)}
.fp3{left:778px;width:392px;background:linear-gradient(150deg,#8c8a80,#b99d7b 50%,#c7b253)}

/* Help */
.help{top:2865px;height:375px;background:var(--sand)}
.help h2{position:absolute;left:46px;top:84px;font-size:32px}
.help-cols{position:absolute;left:46px;top:150px;display:flex;gap:0}
.help-col{width:264px;padding-right:30px}
.help-col h3{font-size:21px;line-height:27px}
.help-col p{margin-top:12px;font-size:11px;line-height:18px;color:var(--ink-soft)}
.partner-card{position:absolute;left:877px;top:93px;width:214px;height:210px;background:var(--blue);border-radius:8px;padding:32px 22px;color:var(--white);box-shadow:0 12px 24px rgba(0,0,0,.18)}
.partner-card h3{font-size:26px;line-height:30px;font-weight:400}
.partner-card svg{margin-top:24px}

/* Testimonials */
.voices{top:3240px;height:542px;background:#fafafb;overflow:hidden}
.quote{position:absolute;top:87px;height:320px;border-radius:18px;padding:58px 34px;background:var(--card-grey);font-size:15px;line-height:22.5px}
.q1{left:22px;width:686px}
.q2{left:720px;width:560px}
.avatar{width:64px;height:64px;border-radius:50%;margin-bottom:34px}
.a1{background:linear-gradient(135deg,#c9a88c,#7a5a46)}
.a2{background:linear-gradient(135deg,#e08a3c,#6b4330)}
.quote cite{display:block;margin-top:22px;font-style:normal;font-size:12px;color:var(--ink-soft)}
.arrows{position:absolute;left:22px;top:436px;display:flex;gap:14px}
.arrow{width:32px;height:32px;border-radius:50%;display:flex;align-items:center;justify-content:center}
.arrow.on{background:var(--blue)}
.arrow.off{background:var(--blue-soft)}

/* Movement */
.movement{top:3782px;height:346px}
.map{position:absolute;inset:0;background:linear-gradient(160deg,#dfe6dc 0%,#e8ece4 50%,#e3e8df 100%)}
.pin{position:absolute;left:546px;top:152px}
.movement-card{position:absolute;left:660px;top:56px;width:412px;height:234px;background:var(--card-warm);border-radius:14px;padding:26px 28px}
.movement-card h2{font-size:22px}
.movement-card p{margin-top:14px;font-size:11.5px;line-height:19.5px;color:var(--ink-soft)}
.movement-card .place{margin-top:12px;font-size:12px}

/* Contact */
.contact{top:4128px;height:431px;background:var(--sand)}
.contact h2{position:absolute;left:42px;top:72px;width:500px;font-size:22px;line-height:28px}
.form{position:absolute;left:586px;top:72px;width:490px}
.row{display:flex;gap:14px}
.field{flex:1;margin-bottom:16px}
.field label{display:block;font-size:10px;margin-bottom:6px}
.field span{display:block;height:28px;background:var(--field);border-radius:3px}
.field.tall span{height:92px}
.form-foot{display:flex;justify-content:space-between;align-items:flex-start;margin-top:4px}
.submit{font-size:11px;padding:6px 12px;border:1.5px solid var(--ink);border-radius:3px;background:var(--white)}
.legal{font-size:8px;line-height:11px;text-align:right;color:var(--ink-soft)}
.legal b{color:var(--ink)}

/* Footer */
.site-footer{top:4559px;height:263px;background:var(--night);color:var(--white)}
.site-footer .tag{position:absolute;left:36px;top:63px;font-size:15px}
.foot-links{position:absolute;left:512px;top:66px;display:flex;gap:18px;list-style:none;font-size:11px}
.notes{position:absolute;left:36px;top:112px;width:340px;font-size:10.5px;line-height:19.5px}
</style>
</head>
<body>

<header class="hero">
  <div class="hero-photo" role="img" aria-label="Smiling diverse college students gathered around a laptop on campus"></div>
  <div class="hero-shade"></div>
  <nav class="nav">
    <div class="brand">Brelvo Quad</div>
    <ul class="nav-links">
      <li>Our Story</li><li>Current State</li><li>Future State</li><li>How You Can Help</li><li>The Movement</li><li>Get Involved</li>
    </ul>
    <span class="nav-cta">Join the Movement</span>
  </nav>
  <div class="hero-copy">
    <h1 class="heading">Guiding Students to Financial Freedom</h1>
    <p>Every year, millions of college students step into adulthood without the skills to manage money wisely. It’s time to change that.</p>
    <span class="btn">Join the Movement</span>
  </div>
</header>

<section class="story">
  <h2 class="heading">Empowering Students.<br>Transforming Futures.</h2>
  <div class="body">
    <p>For too long, financial literacy has been the missing piece of higher education. While students prepare academically for their futures, many graduate with financial stress, poor money habits, and debt that follows them for decades.</p>
    <p>We believe knowledge is power — and financial literacy is freedom. With decades of combined experience in banking, leadership, and higher education, our team has seen the struggles firsthand. That’s why we’re committed to starting a movement that ensures every student leaves college not only with a degree, but with financial confidence.</p>
  </div>
  <div class="story-photo" role="img" aria-label="Group of students with backpacks sharing notes outdoors on campus"></div>
</section>

<section class="current">
  <h2 class="heading">The Current State</h2>
  <div class="stats">
    <div class="stat">
      <div class="stat-card"><div class="stat-icon" role="img" aria-label="Line icon of a stressed person"></div></div>
      <div class="stat-value">70%</div>
      <p class="stat-note">of college students report finances as their #1 source of stress.*</p>
    </div>
    <div class="stat">
      <div class="stat-card"><div class="stat-icon" role="img" aria-label="Line icon of a credit score gauge"></div></div>
      <div class="stat-value">43%</div>
      <p class="stat-note">of students don’t know their credit score.**</p>
    </div>
    <div class="stat">
      <div class="stat-card"><div class="stat-icon" role="img" aria-label="Line icon of a debt document with coins"></div></div>
      <div class="stat-value">$1.7 trillion</div>
      <p class="stat-note">in student loan debt has surpassed</p>
    </div>
  </div>
</section>

<section class="future">
  <h2 class="heading">The Future State (Vision)</h2>
  <div class="body">
    <p>Imagine a campus where students graduate with more than a degree — they graduate with financial confidence.</p>
    <p>They know how to budget, save, manage credit, and plan for their futures. They are free from fear, better equipped for life after graduation, and ready to thrive personally and professionally.</p>
    <p>This is the future we are building together.</p>
  </div>
  <div class="future-photo fp1" role="img" aria-label="Students studying together in a library"></div>
  <div class="future-photo fp2" role="img" aria-label="Two students talking over a laptop outdoors"></div>
  <div class="future-photo fp3" role="img" aria-label="Friends laughing together on campus steps"></div>
</section>

<section class="help">
  <h2 class="heading">How You Can Help</h2>
  <div class="help-cols">
    <div class="help-col"><h3 class="heading">Universities</h3><p>Partner with us to bring scalable, student-centered financial education to your campus</p></div>
    <div class="help-col"><h3 class="heading">Banks &amp; Financial Institutions</h3><p>Join us in shaping the next generation of financially confident customers while strengthening community impact.</p></div>
    <div class="help-col"><h3 class="heading">Students &amp; Parents</h3><p>Be part of a movement that makes the college experience stronger, not harder.</p></div>
  </div>
  <div class="partner-card">
    <h3 class="heading">Contact Us to Partner</h3>
    <svg width="38" height="38" viewBox="0 0 38 38"><circle cx="19" cy="19" r="18" fill="#fff"/><path d="M11 19h13M19 13l7 6-7 6" fill="none" stroke="#1f4fb0" stroke-width="3" stroke-linecap="round" stroke-linejoin="round"/></svg>
  </div>
</section>

<section class="voices">
  <blockquote class="quote q1">
    <div class="avatar a1" role="img" aria-label="Portrait photo of student"></div>
    Brelvo Quad transformed my financial habits! The workshops are engaging and insightful, empowering me with the skills to manage money smartly. I feel more confident about my financial future thanks to their dedicated team in Nairobi.
    <cite>- Amani Kerubo</cite>
  </blockquote>
  <blockquote class="quote q2">
    <div class="avatar a2" role="img" aria-label="Portrait photo of student"></div>
    Brelvo Quad has been a game-changer for me. The financial workshops in Nairobi are practical and insightful. I now budget and save consistently, setting a strong foundation for my future.
    <cite>- Daniel Otieno</cite>
  </blockquote>
  <div class="arrows">
    <span class="arrow on"><svg width="14" height="14" viewBox="0 0 14 14"><path d="M12 7H2M6 3 2 7l4 4" fill="none" stroke="#fff" stroke-width="1.6" stroke-linecap="round" stroke-linejoin="round"/></svg></span>
    <span class="arrow off"><svg width="14" height="14" viewBox="0 0 14 14"><path d="M2 7h10M8 3l4 4-4 4" fill="none" stroke="#1f4fb0" stroke-width="1.6" stroke-linecap="round" stroke-linejoin="round"/></svg></span>
  </div>
</section>

<section class="movement">
  <div class="map" role="img" aria-label="Street map showing the movement location"></div>
  <svg class="pin" width="18" height="24" viewBox="0 0 18 24"><path d="M9 1C4.6 1 1 4.4 1 8.8 1 14.5 9 23 9 23s8-8.5 8-14.2C17 4.4 13.4 1 9 1z" fill="#6a7184"/><circle cx="9" cy="9" r="3" fill="#fff"/></svg>
  <div class="movement-card">
    <h2 class="heading">The Movement</h2>
    <p>This isn’t about one campus — it’s about a shift. A national movement to change the financial future for an entire generation. Together, we can rewrite the story.<br>We believe when students understand money, they reduce stress, gain freedom, and unlock their potential. That’s why this is more than a program — it’s a movement.</p>
    <div class="place">United States</div>
  </div>
</section>

<section class="contact">
  <h2 class="heading">Are you a university leader, bank executive, student, or parent who wants to be part of this movement? Let’s talk.</h2>
  <div class="form">
    <div class="row">
      <div class="field"><label>Name</label><span></span></div>
      <div class="field"><label>Email</label><span></span></div>
    </div>
    <div class="field"><label>Role</label><span></span></div>
    <div class="field tall"><label>Message</label><span></span></div>
    <div class="form-foot">
      <span class="submit">Submit Interest</span>
      <p class="legal">This site is protected by FormGuard and the Veritab <b>Privacy Policy</b><br>and <b>Terms of Service</b> apply.</p>
    </div>
  </div>
</section>

<footer class="site-footer">
  <p class="tag">Join us in building the future of financial literacy.</p>
  <ul class="foot-links">
    <li>Our Story</li><li>Current State</li><li>Future State</li><li>How You Can Help</li><li>The Movement</li><li>Get Involved</li>
  </ul>
  <div class="notes">
    <p>* Norwell Scholastic Wellness Guild, Kestrin Student Vitality Survey, Spring 2022 Report.</p>
    <p>** DALMOR &amp; Pexton Pension Partners, Coins Count at School Review (2019).</p>
    <p>*** Quillan Monetary Trust of Harbridge, Consumer Credit Data (2024).</p>
  </div>
</footer>

</body>
</html>
```